KRT World Class Organisation Poster

We are looking for ideas on how to design this poster to best capture the message we are trying to convey (KRT World Class Organisation). Make sure that these 5 statements feature on the poster.

Logo has been provided, please include in your poster design.

Please use the logo design as the inspiration for your poster layout, drawing on the DNA double helix symbol.

Also refer to the layout of the attached poster. We would like to retain the layout however it should be visually appealing - use your imagination & creativity!
Updates

Updated design brief & extended deadline.

Target Market(s)

internal company use only - logo provided which will need to be included.

Requirements
Must have
• The poster should be in portrait format as it will be printed in 'A3' size.

Must include the KRT logo provided - see attached file.
Nice to have
• Please use the logo design as the inspiration for your poster layout, drawing on the DNA double helix symbol.

```html
<!DOCTYPE html>
<html lang="en">
<head>
<meta charset="utf-8">
<title>KRT World Class Organisation Poster</title>
<link href="https://fonts.googleapis.com/css2?family=Inter:ital,wght@0,100;0,300;0,700;0,800;0,900;1,100;1,300;1,700;1,900&display=swap" rel="stylesheet">
<style>
  :root {
    --backdrop: #e8e5e1;
    --paper: #ffffff;
    --ink: #1c1c1c;
    --ink-soft: #3a3a3a;
    --numeral: #4a4a4a;
    --rule: #2a2a2a;
    --tag-panel: #e4e4e6;
    --tag-text: #8a8a8e;
  }
  * { margin: 0; padding: 0; box-sizing: border-box; }
  html, body {
    width: 1200px; height: 1000px; overflow: hidden;
    background: var(--backdrop);
    font-family: "Inter", Arial, sans-serif;
    color: var(--ink);
  }
  .poster {
    position: absolute; left: 303px; top: 70px;
    width: 622px; height: 875px;
    background: var(--paper);
  }
  .poster > * { position: absolute; white-space: nowrap; line-height: 1; }
  .rule { left: 0; width: 622px; height: 2px; background: var(--rule); }
  .numeral { font-weight: 100; color: var(--numeral); }
  .heavy { font-weight: 900; letter-spacing: -0.5px; }
  .bold { font-weight: 700; }
  .bold-italic { font-weight: 700; font-style: italic; }
  .light-italic { font-weight: 300; font-style: italic; color: var(--ink-soft); }
  .vertical { transform: rotate(-90deg); transform-origin: left top; }
  .right { text-align: right; }

  .tag-panel { left: 482px; top: 0; width: 140px; height: 180px; background: var(--tag-panel); border-left: 2px solid var(--rule); }
  .tag-name { left: 488px; top: 70px; font-size: 32px; font-weight: 900; }
  .tag-line { left: 489px; font-size: 11px; font-style: italic; font-weight: 300; color: var(--tag-text); }
</style>
</head>
<body>
<main class="poster">
  <!-- Statement 1 -->
  <span class="numeral" style="left:22px; top:22px; font-size:132px;">1</span>
  <span class="bold-italic vertical" style="left:76px; top:168px; font-size:20px;">We employ</span>
  <span class="heavy" style="left:109px; top:30px; font-size:30px;">WORLD CLASS</span>
  <span class="heavy" style="left:109px; top:66px; font-size:30px;">BUSINESS SYSTEMS</span>
  <span class="light-italic" style="left:109px; top:98px; font-size:21px;">to exceed expectations by</span>
  <span class="light-italic" style="left:109px; top:122px; font-size:21px;">DRIVING INNOVATION</span>
  <span class="bold-italic" style="left:109px; top:147px; font-size:18px;">at the forefront of technology.</span>

  <div class="tag-panel"></div>
  <span class="tag-name">KRT</span>
  <span class="tag-line" style="top:108px;">IS A</span>
  <span class="tag-line" style="top:126px;">WORLD</span>
  <span class="tag-line" style="top:144px;">CLASS</span>
  <span class="tag-line" style="top:162px;">ORGANISATION</span>

  <div class="rule" style="top:179px;"></div>

  <!-- Statement 2 -->
  <span class="bold-italic" style="left:55px; top:198px; font-size:18px;">We manufacture using</span>
  <span class="heavy" style="left:255px; top:193px; font-size:25px;">INNOVATIVE</span>
  <span class="heavy" style="left:55px; top:218px; font-size:52px; letter-spacing:-2px;">WORLD CLASS</span>
  <span class="heavy" style="left:55px; top:271px; font-size:22px;">MANUFACTURING PROCESSES</span>
  <span class="light-italic right" style="right:168px; top:299px; font-size:15px;">AND lean technologies adapted to produce safe,</span>
  <span class="light-italic right" style="right:168px; top:319px; font-size:13px;">effective + reliable products to meet our patients' needs.</span>
  <span class="numeral" style="left:468px; top:195px; font-size:152px;">2</span>

  <div class="rule" style="top:344px;"></div>

  <!-- Statement 3 -->
  <span class="numeral" style="left:88px; top:350px; font-size:124px;">3</span>
  <span class="bold vertical" style="left:170px; top:450px; font-size:10px;">We strive to be</span>
  <span class="heavy" style="left:192px; top:368px; font-size:42px; letter-spacing:-1px;">WORLD CLASS</span>
  <span class="heavy" style="left:192px; top:410px; font-size:42px; letter-spacing:1px;">COLLEAGUES</span>
  <span class="bold-italic right" style="right:80px; top:455px; font-size:13px;">who are professional, motivated, helpful &amp; positive.</span>
  <span class="light-italic" style="left:95px; top:474px; font-size:17px;">WE ARE ACCOUNTABLE IN ACHIEVING OUR GOALS</span>
  <span class="bold" style="left:97px; top:496px; font-size:18px;">We are innovative, always challenge the</span>
  <span class="bold" style="left:97px; top:520px; font-size:22px;">status-quo + OPEN TO NEW IDEAS.</span>

  <div class="rule" style="top:546px;"></div>

  <!-- Statement 4 -->
  <span class="bold-italic" style="left:172px; top:562px; font-size:20px;">We work with</span>
  <span style="left:313px; top:558px; font-size:24px; font-weight:900; font-style:italic;">WORLD CLASS</span>
  <span style="left:45px; top:583px; font-size:46px; font-weight:900; font-style:italic; letter-spacing:-1px;">SERVICE PROVIDERS</span>
  <span class="light-italic right" style="right:135px; top:628px; font-size:17px;">who are leaders and innovators that challenge</span>
  <span class="light-italic right" style="right:135px; top:650px; font-size:17px;">the status-quo &amp; focus on quality excellence</span>
  <span class="light-italic right" style="right:135px; top:673px; font-size:12px;">and continuous improvement to exceed customer expectations.</span>
  <span class="numeral" style="left:482px; top:552px; font-size:144px;">4</span>

  <div class="rule" style="top:699px;"></div>

  <!-- Statement 5 -->
  <span class="numeral" style="left:48px; top:700px; font-size:156px;">5</span>
  <span class="bold-italic" style="left:152px; top:708px; font-size:20px;">We believe</span>
  <span class="heavy" style="left:152px; top:730px; font-size:37px;">WORLD CLASS</span>
  <span class="heavy" style="left:152px; top:770px; font-size:25px;">CUSTOMER SERVICE</span>
  <span class="heavy" style="left:152px; top:796px; font-size:24px; font-weight:800;">is to deliver the ultimate</span>
  <span class="light-italic" style="left:152px; top:822px; font-size:27px; color:var(--ink);">customer satisfaction every time.</span>
</main>
</body>
</html>
```